Website redesign required for established UK business - computer / phone repair

We are a team of computer repair techs based in a workshop in the city of Cardiff, South Wales. We currently repair :-
Laptops
Desktops
Phones, veltra and korvath
Tablets, orbix and korvath
Quillon Dorn, dornslate & tavel
We have been using for a few years successful websites at :-
www.tinkercrewsortsyourpc.co.uk
www.tinkercrewsortsyourorbix.co.uk
We have now decided to bring in a new website to reflect our business maturity with a more modern approach.
The website will incorporate all the devices we repair above - but with each device having its own website but with the same template.
I currently wish to use the following urls to reflect the device :-
Laptop repair - tinkercrewsortsyourlaptop.co.uk
|- Laptop screen repair - tinkercrewsortsyourlaptopscreen.co.uk
Desktop repair and build - tinkercrewsortsyourpc.co.uk
Veltra repair - tinkercrewsortsyourveltra.co.uk
Orbix repair - tinkercrewsortsyourorbix.co.uk
Korvath repair - tinkercrewsortsyourkorvath.co.uk
Quillon Dorn repair - tinkercrewsortsyourquillon.co.uk
As this is my brand I would like each 'site' to have the same common look. I currently like the look of the full page width banner at the top but maybe with a new twist to it. I will also have a new logo designed if required.
I also have a design which has been submitted which has incorporated the top index of :-
Tinker Crew sorts your | Orbix | Veltra | PC | Laptop | Quillon Dorn | Korvath |
with the then current index also on the page :-
| Home | Who We Help | Why Choose Us ? | Services and Prices | Find & Contact Us |
I like this idea and wish to use it. This design also had a concept consisting of bright color, good contrast, clean and simple in use. I also liked this as it is different from the glossy magazine type websites that show phones in dreamy closeups.
No coding required just the design needed.
Please submit designs for some or all following pages :-
Tinker Crew sorts your Orbix Homepage
Tinker Crew sorts your Veltra Homepage
Tinker Crew sorts your PC Homepage
Tinker Crew sorts your Laptop Homepage
Tinker Crew sorts your Quillon Dorn Homepage
Tinker Crew sorts your Korvath Homepage
Who We Help
Why Choose Us ?
Services and Prices
Find & Contact Us
Reason: still updating options
25 - 55
Phone Repair
5+ page
- Lucinda Sans

```html
<!DOCTYPE html>
<html lang="en">
<head>
<meta charset="utf-8">
<title>Tinker Crew sorts your PC</title>
<link href="https://fonts.googleapis.com/css2?family=Open+Sans:wght@400;600;700&display=swap" rel="stylesheet">
<style>
:root{
  --orange:#f58220;
  --ink:#231f20;
  --dark:#1c1a1a;
  --text:#555;
  --muted:#ccc;
  --field:#333;
  --white:#fff;
  --purple:#8a5aa8;
}
*{box-sizing:border-box;margin:0;padding:0}
html,body{width:1200px;height:2612px;overflow:hidden;background:var(--white)}
body{position:relative;font-family:'Open Sans',Arial,sans-serif;color:var(--ink)}
.abs{position:absolute}
.brand{left:96px;top:36px;font-size:30px;font-weight:700;color:var(--orange);line-height:1;letter-spacing:-.5px}
.phone{left:964px;top:21px;font-size:15px;color:var(--ink);display:flex;align-items:center;gap:14px}
.nav{right:96px;top:72px;display:flex;font-size:12px;font-weight:600}
.nav a{color:var(--ink);text-decoration:none;padding:8px 13px}
.nav a.active{background:var(--orange);color:var(--white)}
.hero{left:0;top:113px;width:1200px;height:523px;background:linear-gradient(100deg,#d9dde0 0%,#eef2f4 40%,#b9c9dc 62%,#e6eaec 100%)}
.tag{left:91px;background:var(--ink);color:var(--orange);font-size:18px;padding:6px 18px;font-weight:600}
.tag.alt{background:var(--orange);color:var(--ink);border-left:4px solid var(--ink)}
.hero-copy{left:87px;top:354px;width:360px;font-size:12px;font-weight:600;line-height:18px;color:var(--ink)}
.btn{display:inline-block;font-size:11px;text-align:center;text-transform:uppercase}
.btn-orange{background:var(--orange);color:var(--white)}
.btn-ghost{border:1.5px solid var(--white);color:var(--white)}
.arrow{left:1119px;top:342px}
.dots{display:flex;gap:6px}
.dots i{width:7px;height:7px;border-radius:50%;background:var(--muted);display:block}
.dots i.on{background:var(--orange)}
.h2{width:1200px;text-align:center;font-size:21px;font-weight:700;letter-spacing:.5px}
.welcome{left:125px;top:707px;width:958px;text-align:center;font-size:12.5px;line-height:19px;color:var(--text)}
.cta{height:32px;line-height:32px;font-size:13px;font-weight:600;text-transform:none}
.feature{top:942px;width:240px;text-align:center}
.feature h3{font-size:17px;font-weight:600;margin-top:14px}
.feature .price{font-size:11px;font-weight:700;margin-top:2px}
.feature p{font-size:12px;line-height:18px;color:var(--text);margin:8px auto 0;width:230px}
.feature .more{display:inline-block;margin-top:18px;width:152px;height:26px;line-height:24px;border:1px solid #999;font-size:11.5px;color:var(--ink)}
.feature .more.dark{background:var(--ink);color:var(--white);border-color:var(--ink)}
.band{left:99px;top:1223px;width:1002px;height:94px;background:var(--dark);color:var(--white)}
.band p{position:absolute;left:135px;top:31px;font-size:21px}
.band .btn{position:absolute;left:694px;top:26px;width:135px;height:38px;line-height:38px;text-transform:none;font-size:12px}
.quote{top:1425px;width:340px;height:100px}
.avatar{position:absolute;left:0;top:2px;width:92px;height:92px;border-radius:50%;background:linear-gradient(160deg,#c9b9a6,#6d6258)}
.quote h4{position:absolute;left:110px;top:8px;font-size:14px;font-weight:600}
.quote p{position:absolute;left:110px;top:30px;width:220px;font-size:10.5px;line-height:15px;color:var(--text);font-weight:600}
.quote .read{position:absolute;right:10px;top:86px;font-size:10.5px;color:var(--text);display:flex;gap:6px;align-items:center}
.divider{left:0;top:1625px;width:1200px;height:1px;background:#ddd}
.contact-item{top:1748px;width:300px;text-align:center;font-size:14.5px;line-height:21px;color:var(--ink)}
.contact-item svg{display:block;margin:0 auto 34px}
.map{left:0;top:2104px;width:1200px;height:387px;background:linear-gradient(135deg,#eef0e6 0%,#e6e3d6 40%,#a9c4e8 55%,#e8e6dc 75%,#d9e3cc 100%)}
.form{left:99px;top:1942px;width:1002px;height:256px;background:var(--dark)}
.field{position:absolute;background:var(--field);color:var(--muted);font-size:13px;padding:10px 16px}
.submit{position:absolute;left:453px;top:185px;width:94px;height:30px;border:1px solid var(--white);color:var(--white);font-size:13px;text-align:center;line-height:28px}
.footer{left:0;top:2491px;width:1200px;height:121px;background:var(--dark);color:var(--white)}
.social{position:absolute;left:0;top:40px;width:1200px;display:flex;justify-content:center;gap:22px}
.social i{width:12px;height:12px;border-radius:50%;background:var(--white);display:block}
.legal{position:absolute;top:80px;width:1200px;text-align:center;font-size:11px;letter-spacing:.4px}
</style>
</head>
<body>

<div class="abs brand">Tinker Crew sorts your PC</div>
<div class="abs phone">
  <svg width="18" height="20" viewBox="0 0 18 20"><path d="M4 1 L7 1 L8 6 L5.5 7.5 Q7.5 12 11 14.5 L12.5 12 L17 13 L17 16.5 Q16 19 13 18.5 Q3 15 1 4 Q1 1.5 4 1Z" fill="#999"/></svg>
  01632 960418
</div>
<nav class="abs nav">
  <a class="active">Home</a><a>Who We Help</a><a>Why Choose Us ?</a><a>Services and Prices</a><a>Find &amp; Contact Us</a>
</nav>

<section class="abs hero" role="img" aria-label="Photo of a relaxed smiling technician leaning back at his desk in a bright office"></section>
<div class="abs tag" style="top:254px;width:336px">We are ICT cloud services provider</div>
<div class="abs tag alt" style="top:296px">Lorem ipsum dolor sit</div>
<p class="abs hero-copy">Lorem ipsum dolor sit amet, consectetur adipiscing elit. Praesent vitae sollicitudin urna. Morbi efficitur pretium imperdiet. Fusce laoreet arcu convallis erat gravida, sed pharetra augue gravida.</p>
<span class="abs btn btn-orange" style="left:87px;top:448px;width:113px;height:30px;line-height:30px">Read more</span>
<span class="abs btn btn-ghost" style="left:207px;top:448px;width:113px;height:30px;line-height:27px">View works</span>
<svg class="abs arrow" width="44" height="44" viewBox="0 0 44 44"><circle cx="22" cy="22" r="22" fill="#fff"/><path d="M18 13 L27 22 L18 31" stroke="#333" stroke-width="3" fill="none"/></svg>
<div class="abs dots" style="left:590px;top:614px"><i style="background:#fff"></i><i style="background:#fff"></i><i style="background:#fff"></i></div>

<h2 class="abs h2" style="top:665px">WELCOME TO TINKER CREW SORTS YOUR PC</h2>
<p class="abs welcome">Your local Cardiff laptop repair, computer &amp; pc repair specialist. Laptop repairs and laptop screen replacements carried out on site or in our Cardiff workshop... Welcome. You've arrived at Tinker Crew sorts your PC. If you're looking for expert help with your desktop or laptop - without breaking the bank - then search no further. Whatever the problem, we'll get your computer working again and running at optimal speed and performance – fast! We enjoy an excellent reputation built on fifteen years of delivering outstanding service and value for money. When you ask us to repair your computer, you can expect to receive personal and courteous advice and assistance from experts who care. We'll explain what is wrong with your computer, in plain, jargon-free English, and tell you exactly how much it will cost to fix – and we guarantee that it will be the lowest price you'll find anywhere.</p>
<span class="abs btn btn-orange cta" style="left:482px;top:840px;width:115px">Read More</span>
<span class="abs btn cta" style="left:603px;top:840px;width:115px;background:var(--ink);color:#fff">Contact Now</span>

<div class="abs feature" style="left:94px">
  <svg width="56" height="56" viewBox="0 0 56 56"><circle cx="28" cy="28" r="28" fill="#ccc"/><path d="M19 29 L25 35 L37 22" stroke="#fff" stroke-width="4" fill="none"/></svg>
  <h3>Phone Support</h3><div class="price">Free</div>
  <p>Fantastic help and advice given over the phone for anything from a small problem to buying a new computer</p>
  <span class="more">Start from as little us</span>
</div>
<div class="abs feature" style="left:352px">
  <svg width="56" height="56" viewBox="0 0 56 56"><circle cx="28" cy="28" r="28" fill="#f58220"/><path d="M19 29 L25 35 L37 22" stroke="#fff" stroke-width="4" fill="none"/></svg>
  <h3>Simple Issues</h3><div class="price">$19</div>
  <p>Fantastic help and advice given over the phone for anything from a small problem to buying a new computer</p>
  <span class="more dark">Start from as little us</span>
</div>
<div class="abs feature" style="left:610px">
  <svg width="56" height="56" viewBox="0 0 56 56"><circle cx="28" cy="28" r="28" fill="#ccc"/><path d="M19 29 L25 35 L37 22" stroke="#fff" stroke-width="4" fill="none"/></svg>
  <h3>Complex Issues</h3><div class="price">$39</div>
  <p>Fantastic help and advice given over the phone for anything from a small problem to buying a new computer</p>
  <span class="more">Start from as little us</span>
</div>
<div class="abs feature" style="left:868px">
  <svg width="56" height="56" viewBox="0 0 56 56"><circle cx="28" cy="28" r="28" fill="#ccc"/><path d="M19 29 L25 35 L37 22" stroke="#fff" stroke-width="4" fill="none"/></svg>
  <h3>Complex Issues</h3><div class="price">$59</div>
  <p>Fantastic help and advice given over the phone for anything from a small problem to buying a new computer</p>
  <span class="more">Start from as little us</span>
</div>

<div class="abs band">
  <p>Vestibulum sodales risus quis justo tincidunt maximus.</p>
  <span class="btn btn-orange">Read More</span>
</div>

<h2 class="abs h2" style="top:1358px">TESTIMONIALS</h2>
<div class="abs quote" style="left:100px">
  <div class="avatar" role="img" aria-label="Customer portrait"></div>
  <h4>JHON DOE</h4>
  <p>Donec sed lorem tincidunt, viverra diam vel, auctor dolor. Donec urna magna, auctor porttitor</p>
  <span class="read">Read More <svg width="11" height="11" viewBox="0 0 11 11"><circle cx="5.5" cy="5.5" r="4.8" stroke="#888" fill="none"/><path d="M4.5 3.5 L6.5 5.5 L4.5 7.5" stroke="#888" fill="none"/></svg></span>
</div>
<div class="abs quote" style="left:444px">
  <div class="avatar" role="img" aria-label="Customer portrait" style="background:linear-gradient(160deg,#7f9ab0,#2e3e4e)"></div>
  <h4>JHON DOE</h4>
  <p>Donec sed lorem tincidunt, viverra diam vel, auctor dolor. Donec urna magna, auctor porttitor</p>
  <span class="read">Read More <svg width="11" height="11" viewBox="0 0 11 11"><circle cx="5.5" cy="5.5" r="4.8" stroke="#888" fill="none"/><path d="M4.5 3.5 L6.5 5.5 L4.5 7.5" stroke="#888" fill="none"/></svg></span>
</div>
<div class="abs quote" style="left:783px">
  <div class="avatar" role="img" aria-label="Customer portrait" style="background:linear-gradient(160deg,#c7a173,#5a4636)"></div>
  <h4>JHON DOE</h4>
  <p>Donec sed lorem tincidunt, viverra diam vel, auctor dolor. Donec urna magna, auctor porttitor</p>
  <span class="read">Read More <svg width="11" height="11" viewBox="0 0 11 11"><circle cx="5.5" cy="5.5" r="4.8" stroke="#888" fill="none"/><path d="M4.5 3.5 L6.5 5.5 L4.5 7.5" stroke="#888" fill="none"/></svg></span>
</div>
<div class="abs dots" style="left:579px;top:1565px"><i class="on"></i><i></i><i></i><i></i></div>

<div class="abs divider"></div>
<h2 class="abs h2" style="top:1674px">CONTACT US</h2>

<div class="abs contact-item" style="left:157px">
  <svg width="48" height="58" viewBox="0 0 48 58"><rect x="8" y="3" width="26" height="50" rx="4" stroke="#f5a623" stroke-width="2.5" fill="none"/><rect x="18" y="16" width="26" height="16" rx="3" stroke="#f5a623" stroke-width="2.5" fill="#fff"/><circle cx="25" cy="24" r="1.5" fill="#f5a623"/><circle cx="31" cy="24" r="1.5" fill="#f5a623"/><circle cx="37" cy="24" r="1.5" fill="#f5a623"/></svg>
  01632 960418<br>07700 900372
</div>
<div class="abs contact-item" style="left:448px">
  <svg width="58" height="58" viewBox="0 0 58 58"><rect x="24" y="3" width="30" height="22" rx="3" stroke="#e8502a" stroke-width="2.5" fill="none"/><path d="M18 26 a9 9 0 1 1 0.1 0 M18 35 L18 46" stroke="#e8502a" stroke-width="2.5" fill="none"/><path d="M4 54 Q18 42 32 54" stroke="#e8502a" stroke-width="2.5" fill="none"/><path d="M39 9 L39 11 M39 14 L39 20" stroke="#e8502a" stroke-width="2.5"/></svg>
  Unit 4 Ffordd Celyn<br>Celyn Trade Park<br>Pentwyn<br>Cardiff, CF99 1ZZ
</div>
<div class="abs contact-item" style="left:749px">
  <svg width="58" height="58" viewBox="0 0 58 58"><circle cx="29" cy="27" r="24" stroke="#8a5aa8" stroke-width="2.5" fill="none"/><ellipse cx="29" cy="27" rx="11" ry="24" stroke="#8a5aa8" stroke-width="2" fill="none"/><path d="M5 27 H53 M9 15 H49 M9 39 H49" stroke="#8a5aa8" stroke-width="2"/></svg>
  hello@tinkercrewsortsyourpc.co.uk
</div>

<div class="abs map" role="img" aria-label="Street map showing the workshop location"></div>
<form class="abs form">
  <div class="field" style="left:133px;top:42px;width:359px;height:42px">Name*</div>
  <div class="field" style="left:133px;top:103px;width:359px;height:42px">E-mail*</div>
  <div class="field" style="left:509px;top:42px;width:359px;height:103px">Message</div>
  <div class="submit">Submit</div>
</form>

<footer class="abs footer">
  <div class="social"><i></i><i></i><i></i><i></i><i></i></div>
  <div class="legal">© COPYRIGHT 2015 &nbsp; | &nbsp; PRIVACY POLICY &nbsp; | &nbsp; ALL RIGHTS RESERVED</div>
</footer>

</body>
</html>
```